Stationary - Business Card/Letterhead and envelope design

Details for my new Stationery Design Project will be added soon. , I have two logos I am trying to decide on. I will upload the eps logos shortly. I have attached a file of what i have so far. I need urgently Business cards, but also will need a letterhead template and envelopes.

PLEASE NOTE THE DEADLINE SAYS 2 DAYS but I need business card design in LESS THAN A DAY.

thanks, Details for my new Stationery Design Project will be added soon. , I have two logos I am trying to decide on. I will upload the eps logos shortly. I have attached a file of what i have so far. I need urgently Business cards, but also will need a letterhead template and envelopes.

thanks
Updates

I have uploaded one of the logos you can work with. hopefully the other one comes soon.

details for the business card.

Marnet Dobson

Managing Director

P&K Ventures Ltd

Bda: 1-441-555-0182

Email: marnet@pkvnbda.example

web: www.pkvnbda.example

Industry/Entity Type

Business

```html
<!DOCTYPE html>
<html lang="en">
<head>
<meta charset="utf-8">
<title>P&amp;K Ventures Ltd – Business Card</title>
<link href="https://fonts.googleapis.com/css2?family=PT+Sans:wght@400;700&display=swap" rel="stylesheet">
<style>
  :root {
    --backdrop: #d6d6d6;
    --teal: #2ba3bd;
    --earth: #7b6a55;
    --paper: #ffffff;
    --shadow: rgba(0, 0, 0, 0.25);
  }
  * { margin: 0; padding: 0; box-sizing: border-box; }
  html, body {
    width: 1200px;
    height: 900px;
    overflow: hidden;
    background: var(--backdrop);
    font-family: "PT Sans", sans-serif;
  }
  .stage { position: relative; width: 1200px; height: 900px; }

  .card {
    position: absolute;
    left: 333px;
    width: 502px;
    height: 325px;
    overflow: hidden;
    box-shadow: 0 1px 4px var(--shadow);
  }
  .card--front { top: 90px; background: var(--paper); }
  .card--back { top: 485px; background: var(--teal); }

  .front__band {
    position: absolute;
    top: 0;
    left: 24px;
    width: 164px;
    height: 100%;
    background: var(--teal);
  }
  .front__panel {
    position: absolute;
    top: 0;
    left: 188px;
    right: 0;
    height: 100%;
    background: var(--earth);
    color: var(--paper);
  }

  .brand-disc {
    position: absolute;
    border-radius: 50%;
    background: var(--paper);
    display: flex;
    align-items: center;
    justify-content: center;
  }
  .brand-disc--small { left: 47px; top: 87px; width: 108px; height: 108px; }
  .brand-disc--large { left: 140px; top: 53px; width: 222px; height: 222px; }

  .brand-name {
    color: var(--earth);
    font-weight: 700;
    white-space: nowrap;
  }
  .brand-disc--small .brand-name { font-size: 12px; }
  .brand-disc--large .brand-name { font-size: 25px; }

  .person {
    position: absolute;
    left: 29px;
    top: 108px;
  }
  .person__name {
    font-size: 25px;
    line-height: 1;
    font-weight: 400;
  }
  .person__name strong { font-weight: 700; }
  .person__role {
    font-size: 16px;
    margin-top: 3px;
  }

  .contact {
    position: absolute;
    left: 29px;
    top: 237px;
    list-style: none;
    font-size: 13.5px;
  }
  .contact__item {
    display: flex;
    align-items: center;
    height: 19px;
  }
  .contact__icon {
    width: 15px;
    height: 15px;
    background: var(--paper);
    color: var(--earth);
    font-size: 13px;
    font-weight: 700;
    line-height: 14px;
    text-align: center;
    margin-right: 8px;
  }

  .address {
    position: absolute;
    left: 0;
    right: 0;
    bottom: 17px;
    text-align: center;
    color: var(--paper);
    font-size: 14.5px;
  }
</style>
</head>
<body>
<main class="stage">
  <section class="card card--front" aria-label="Business card front">
    <div class="front__band">
      <div class="brand-disc brand-disc--small">
        <span class="brand-name">P&amp;K Ventures Ltd</span>
      </div>
    </div>
    <div class="front__panel">
      <div class="person">
        <h1 class="person__name">Marnet <strong>Dobson</strong></h1>
        <p class="person__role">CEO</p>
      </div>
      <ul class="contact">
        <li class="contact__item"><span class="contact__icon">p</span>1-441-555-0182</li>
        <li class="contact__item"><span class="contact__icon">m</span>marnet@pkvnbda.example</li>
        <li class="contact__item"><span class="contact__icon">w</span>www.pkvnbda.example</li>
      </ul>
    </div>
  </section>

  <section class="card card--back" aria-label="Business card back">
    <div class="brand-disc brand-disc--large">
      <span class="brand-name">P&amp;K Ventures Ltd</span>
    </div>
    <p class="address">27 Harbour Row, Hamilton HM 11, Bermuda</p>
  </section>
</main>
</body>
</html>
```